business card for author of crime novel

I am an author with a new book. I need a business card with the book's cover on one side (already uploaded), and contact details on the other.

Walt Pemberty
Author

telephone: 646-512-7380
website: www.waltpemberty.net
facebook: friendwall.net/wpemberty
twitter: chirpline.net/wpemberty
email: wpemberty@postvale.net

Target Market(s)

Readers of mystery books

Industry/Entity Type

Business

Contact Information for Business Card

Walt Pemberty
Author

telephone: 646-512-7380

Font styles to use
Serif
Sans Serif

Requirements
Must have
• Book cover on one side. My contact info on the other, with the name of the book repeated if that makes sense. Clean design.
Should not have
• Overly ornate, too formal, too distracting

```html
<!DOCTYPE html>
<html lang="en">
<head>
<meta charset="utf-8">
<title>Walt Pemberty – Business Card</title>
<link href="https://fonts.googleapis.com/css2?family=Russo+One&family=Open+Sans:wght@300;400;700&display=swap" rel="stylesheet">
<style>
  :root {
    --backdrop: #6f6e63;
    --backdrop-dark: #4f4e46;
    --paper-light: #e6e7e9;
    --paper-white: #eef2f4;
    --slate: #4a4d50;
    --ink: #1c1c1c;
    --night-top: #3a3a3a;
    --night-bottom: #141414;
    --name-grey: #d2d2d2;
    --cover-orange: #e0a12a;
    --cover-blue: #6f8596;
    --frame-white: #ffffff;
  }
  * { box-sizing: border-box; margin: 0; padding: 0; }
  html, body { width: 1200px; height: 673px; overflow: hidden; }
  body {
    background: radial-gradient(ellipse at center, var(--backdrop) 0%, var(--backdrop-dark) 100%);
    font-family: "Open Sans", sans-serif;
    position: relative;
  }
  .card {
    position: absolute;
    top: 194px;
    width: 500px;
    height: 285px;
    display: flex;
    overflow: hidden;
    box-shadow: 0 10px 24px rgba(0,0,0,0.4);
  }
  .card--front { left: 60px; }
  .card--back { left: 640px; }

  /* Front */
  .front__title-panel {
    flex: 0 0 62%;
    background: var(--paper-light);
    display: flex;
    align-items: center;
    justify-content: center;
  }
  .book-title {
    font-family: "Russo One", sans-serif;
    font-weight: 400;
    font-size: 20px;
    letter-spacing: 1.5px;
    color: var(--ink);
    white-space: nowrap;
  }
  .front__cover-panel {
    flex: 1;
    background: var(--slate);
    display: flex;
    align-items: center;
    justify-content: center;
  }
  .cover-frame {
    background: var(--frame-white);
    padding: 6px;
    width: 118px;
    height: 168px;
  }
  .cover-art {
    width: 100%;
    height: 100%;
    background:
      linear-gradient(180deg, var(--cover-orange) 0 14%, transparent 14% 86%, var(--cover-orange) 86%),
      linear-gradient(160deg, #8fa3b2 0%, var(--cover-blue) 55%, #4f6271 100%);
    border: 6px solid var(--cover-orange);
    border-top: 0;
    border-bottom: 0;
  }

  /* Back */
  .back__contact-panel {
    flex: 0 0 43%;
    background: var(--paper-white);
    display: flex;
    flex-direction: column;
    justify-content: center;
    padding-left: 22px;
    gap: 13px;
  }
  .contact-row {
    display: flex;
    align-items: center;
    gap: 6px;
    font-size: 9.5px;
    color: var(--ink);
    white-space: nowrap;
  }
  .contact-row svg { width: 11px; height: 11px; flex: 0 0 11px; }
  .back__name-panel {
    flex: 1;
    background: linear-gradient(180deg, var(--night-top), var(--night-bottom));
    display: flex;
    flex-direction: column;
    justify-content: center;
    padding-left: 14px;
  }
  .author-name {
    font-weight: 300;
    font-size: 24px;
    color: var(--name-grey);
    line-height: 1.1;
  }
  .author-role {
    font-weight: 700;
    font-size: 10px;
    color: var(--name-grey);
    margin-top: 1px;
  }
</style>
</head>
<body>

<section class="card card--front">
  <div class="front__title-panel">
    <h1 class="book-title">DEAD LETTER ALLEY</h1>
  </div>
  <div class="front__cover-panel">
    <div class="cover-frame">
      <div class="cover-art" role="img" aria-label="Book cover: orange frame around a blue-toned photograph of an old city apartment building"></div>
    </div>
  </div>
</section>

<section class="card card--back">
  <div class="back__contact-panel">
    <div class="contact-row">
      <svg viewBox="0 0 12 12"><rect x="0.5" y="0.5" width="11" height="11" rx="2" fill="none" stroke="#1c1c1c"/><path d="M3.5 3 L5 3 L5.5 4.5 L4.6 5.1 Q5.4 6.8 6.9 7.4 L7.5 6.5 L9 7 L9 8.5 Q5 9 3.5 3Z" fill="#1c1c1c"/></svg>
      <span>: 646-512-7380</span>
    </div>
    <div class="contact-row">
      <svg viewBox="0 0 12 12"><circle cx="6" cy="6" r="5.5" fill="#1c1c1c"/><ellipse cx="6" cy="6" rx="2.3" ry="5" fill="none" stroke="#eef2f4" stroke-width="0.8"/><line x1="1" y1="6" x2="11" y2="6" stroke="#eef2f4" stroke-width="0.8"/></svg>
      <span>: www.waltpemberty.net</span>
    </div>
    <div class="contact-row">
      <svg viewBox="0 0 12 12"><rect x="1" y="1" width="10" height="10" fill="#1c1c1c"/></svg>
      <span>: friendwall.net/wpemberty</span>
    </div>
    <div class="contact-row">
      <svg viewBox="0 0 12 12"><circle cx="6" cy="6" r="5.5" fill="#1c1c1c"/></svg>
      <span>: chirpline.net/wpemberty</span>
    </div>
    <div class="contact-row">
      <svg viewBox="0 0 12 12"><rect x="0.5" y="2.5" width="11" height="7.5" rx="1" fill="#1c1c1c"/><path d="M1 3 L6 7 L11 3" fill="none" stroke="#eef2f4" stroke-width="0.9"/></svg>
      <span>: wpemberty@postvale.net</span>
    </div>
  </div>
  <div class="back__name-panel">
    <h2 class="author-name">Walt Pemberty</h2>
    <p class="author-role">Author</p>
  </div>
</section>

</body>
</html>
```